Dalworth Construction Needs a Business Card

Our current business card is very bland, and since we have a new logo, we would like a new business card design to reflect our company. It can be a single-sided or two-sided card, but it is important that our contact information appears on the same side. I am attaching a copy of our old card and our new logo. If you need the logo in another format than the one I'm sending, please let me know. This is the information that we must have on our card, but not necessarily in any specific order:
1) Our logo
2) General Contractor
3) Grant Ellsworth, Owner
4) 482 Commerce Loop Road, Centre, Alabama 35914
5) Office: 256-418-7735
7) Fax: 256-418-7736
8) Cell: 256-609-4418
9) dalworthconstruction@qvx.net
10) dalworthconstruction.com (can be omitted if necessary)
Also, I will need files in a format that I can alter if any of the above information changes in the near future. Thank you in advance for your submissions!
Target Market(s)
Commercial and residential clients, architects, and subcontractors.
Industry/Entity Type
Business
Look and feel

```html
<!DOCTYPE html>
<html lang="en">
<head>
<meta charset="utf-8">
<title>Dalworth Construction – Business Card</title>
<link href="https://fonts.googleapis.com/css2?family=Exo+2:wght@400;500;800&display=swap" rel="stylesheet">
<style>
  :root {
    --stage: #2b2b2d;
    --card-light-a: #f7f7f7;
    --card-light-b: #d9d9d9;
    --band-dark: #3b3b3c;
    --ink: #2f2f30;
    --ink-soft: #555;
    --on-dark: #f2f2f2;
    --on-dark-soft: #cfcfcf;
  }
  * { box-sizing: border-box; margin: 0; padding: 0; }
  html, body { width: 1200px; height: 869px; overflow: hidden; }
  body {
    background: var(--stage);
    font-family: "Exo 2", sans-serif;
    display: flex;
    align-items: center;
    justify-content: center;
    gap: 40px;
  }
  .card {
    position: relative;
    width: 540px;
    height: 309px;
    background: linear-gradient(160deg, var(--card-light-a) 0%, var(--card-light-b) 100%);
    overflow: hidden;
    box-shadow: 0 10px 30px rgba(0,0,0,.45);
  }

  /* wordmark */
  .brand { display: flex; align-items: center; gap: 14px; color: var(--ink); }
  .brand-square { width: 54px; height: 54px; background: var(--ink); flex: none; }
  .brand-name {
    font-weight: 800;
    font-size: 38px;
    line-height: .95;
    text-transform: uppercase;
    letter-spacing: .5px;
  }
  .brand-name small { display: block; font-size: 19px; letter-spacing: 5.2px; }

  /* back side */
  .card-back { display: flex; align-items: center; justify-content: center; }

  /* front side */
  .front-contacts {
    position: absolute; left: 30px; top: 24px;
    list-style: none;
    font-size: 11px; color: var(--ink-soft);
    display: grid; gap: 7px;
  }
  .front-contacts li { display: flex; align-items: center; gap: 8px; white-space: nowrap; }
  .front-contacts svg { width: 11px; height: 11px; fill: var(--ink-soft); flex: none; }
  .front-brand { position: absolute; right: 28px; top: 66px; }
  .front-brand .brand-square { width: 46px; height: 46px; }
  .front-brand .brand-name { font-size: 32px; }
  .front-brand .brand-name small { font-size: 16px; letter-spacing: 4.3px; }

  .front-band {
    position: absolute; left: 0; right: 0; bottom: 0; height: 134px;
    background: var(--band-dark);
    color: var(--on-dark);
  }
  .front-address {
    position: absolute; left: 30px; top: 18px;
    font-style: normal; font-size: 13px; line-height: 1.45;
  }
  .front-person { position: absolute; right: 28px; bottom: 22px; text-align: right; }
  .person-name { font-size: 15px; font-weight: 500; text-transform: uppercase; letter-spacing: .5px; }
  .person-role { font-size: 12px; margin-top: 2px; }
  .person-trade { font-size: 11px; margin-top: 1px; color: var(--on-dark-soft); }
</style>
</head>
<body>

  <section class="card card-back" aria-label="Card back">
    <div class="brand">
      <span class="brand-square"></span>
      <span class="brand-name">Dalworth<small>Construction</small></span>
    </div>
  </section>

  <section class="card card-front" aria-label="Card front">
    <ul class="front-contacts">
      <li><svg viewBox="0 0 24 24"><path d="M6.6 10.8a15.1 15.1 0 0 0 6.6 6.6l2.2-2.2c.3-.3.7-.4 1-.2 1.1.4 2.3.6 3.6.6.6 0 1 .4 1 1V20c0 .6-.4 1-1 1A17 17 0 0 1 3 4c0-.6.4-1 1-1h3.5c.6 0 1 .4 1 1 0 1.3.2 2.5.6 3.6.1.3 0 .7-.2 1z"/></svg>Office: 256-418-7735</li>
      <li><svg viewBox="0 0 24 24"><path d="M7 1h10a2 2 0 0 1 2 2v18a2 2 0 0 1-2 2H7a2 2 0 0 1-2-2V3a2 2 0 0 1 2-2zm0 3v14h10V4zm5 15.5a1 1 0 1 0 0 2 1 1 0 0 0 0-2z"/></svg>Cell: 256-609-4418</li>
      <li><svg viewBox="0 0 24 24"><path d="M6 2h12v6H6zM3 9h18a2 2 0 0 1 2 2v7h-4v4H5v-4H1v-7a2 2 0 0 1 2-2zm4 7v4h10v-4z"/></svg>Fax: 256-418-7736</li>
      <li><svg viewBox="0 0 24 24"><path d="M2 5h20v14H2zm2 2v.5l8 5 8-5V7z"/></svg>dalworthconstruction@qvx.net</li>
      <li><svg viewBox="0 0 24 24"><circle cx="12" cy="12" r="10"/></svg>dalworthconstruction.com</li>
    </ul>

    <div class="brand front-brand">
      <span class="brand-square"></span>
      <span class="brand-name">Dalworth<small>Construction</small></span>
    </div>

    <div class="front-band">
      <address class="front-address">482 Commerce Loop Road<br>Centre, Alabama 35914</address>
      <div class="front-person">
        <p class="person-name">Grant Ellsworth</p>
        <p class="person-role">Owner</p>
        <p class="person-trade">General Contractor</p>
      </div>
    </div>
  </section>

</body>
</html>
```